Upbeat Accouting Package Flyer

I am looking for a 1 page (front, or front and back) flyer that will become our marketing for our accounting services. We are looking for something a little different and we are catering to the small retail shop owners. We have 3 accounting packages we would like to display and then some add-ons. I have included our logo that must be included in the design. I have uploaded the accounting package information as well.
Target Market(s)
Small Retail Shop Owners
Industry/Entity Type
Accounting
Colors
Designer to choose colors to be used in the design.
Requirements
Must have
- A casual feel. We are not your typical accountants who are very professional and "stuffy". I want it to feel like we are all family.
Nice to have
- I would like to incorporate some sort of retail theme.
- We have a couple of taglines we like to use and it would be great if they could be included. They are "We know you CAN do the accounting, but do you WANT to?" and "We allow you to get back to what's important."
Should not have
- Typical stock accounting photos of people shaking hands, large office buildings, etc.

```html
<!DOCTYPE html>
<html lang="en">
<head>
<meta charset="utf-8">
<title>Larkfield Tax and Accounting – Accounting Packages</title>
<link rel="stylesheet" href="https://fonts.googleapis.com/css2?family=Roboto+Condensed:wght@400;500;700&display=swap">
<style>
:root{
  --orange:#f5883a;
  --teal:#1fb3dc;
  --ink:#2b2b2b;
  --band:#00aeef;
  --band-light:#6ccbec;
  --grey:#8a8a8a;
  --paper:#ffffff;
}
*{margin:0;padding:0;box-sizing:border-box}
html,body{width:927px;height:1200px;overflow:hidden;background:var(--paper)}
body{font-family:"Roboto Condensed",sans-serif;color:var(--ink);position:relative}
.hero{position:absolute;left:0;top:0;width:927px;height:565px;
  background:
    radial-gradient(ellipse 230px 130px at 230px 330px,rgba(226,190,165,.95) 0%,rgba(226,190,165,.55) 55%,rgba(226,190,165,0) 100%),
    radial-gradient(ellipse 210px 70px at 580px 355px,rgba(70,74,80,.85) 0%,rgba(70,74,80,.4) 60%,rgba(70,74,80,0) 100%),
    radial-gradient(ellipse 160px 90px at 720px 250px,rgba(255,255,255,.9) 0%,rgba(255,255,255,0) 100%),
    radial-gradient(ellipse 420px 110px at 560px 470px,rgba(250,252,253,.95) 0%,rgba(250,252,253,.6) 60%,rgba(250,252,253,0) 100%),
    radial-gradient(ellipse 160px 50px at 330px 470px,rgba(230,196,90,.55) 0%,rgba(230,196,90,0) 100%),
    radial-gradient(ellipse 130px 60px at 800px 470px,rgba(45,150,220,.45) 0%,rgba(45,150,220,0) 100%),
    radial-gradient(ellipse 120px 220px at 30px 380px,rgba(150,185,220,.7) 0%,rgba(150,185,220,0) 100%),
    linear-gradient(170deg,#f1f6f9 0%,#dfeaf1 35%,#cfdfea 65%,#e9f0f4 100%)}
.brand{position:absolute;left:138px;top:82px}
.brand-name{font-size:64px;font-weight:700;color:var(--ink);letter-spacing:1px;line-height:1;display:flex;align-items:center;gap:12px}
.brand-dot{width:18px;height:18px;border-radius:50%;background:var(--teal)}
.brand-sub{margin-left:108px;margin-top:4px;font-size:15px;color:var(--teal);letter-spacing:.5px}
.hero-tag{position:absolute;left:492px;top:93px;width:435px;height:78px;background:rgba(255,255,255,.8);
  padding:12px 0 0 24px;font-size:21px;line-height:29px;color:var(--teal)}
.section-bar{position:absolute;left:0;top:518px;width:370px;height:47px;background:var(--orange);
  color:#fff;font-size:25px;font-weight:500;padding:9px 0 0 112px}
.section-tag{position:absolute;left:398px;top:528px;font-size:20px;color:var(--ink)}
.package{position:absolute}
.package h2{font-size:24px;font-weight:700;color:var(--orange);display:flex;align-items:flex-end;gap:6px;height:30px}
.package h2 small{font-size:18px;font-weight:400}
.list{list-style:none;margin-top:2px}
.list li{position:relative;font-size:15px;line-height:19.7px}
.list li::before{content:">";position:absolute;left:-20px;color:var(--orange);font-weight:700;font-size:13px}
.list sup{font-size:9px;line-height:0;vertical-align:6px}
.list .note{font-size:11px}
.list .plain::before{content:none}
.develop{left:114px;top:592px}
.grow{left:114px;top:790px}
.relax{left:532px;top:592px}
.extras{position:absolute;left:532px;top:884px;width:360px}
.extras h2{font-size:24px;font-weight:700;color:var(--orange);display:flex;align-items:center;gap:14px}
.extras-grid{display:grid;grid-template-columns:203px 150px;row-gap:12px;margin-top:8px}
.extras h3{font-size:16px;font-weight:700;line-height:20px}
.extras .list li{font-size:15px}
.footer{position:absolute;left:0;top:1080px;width:927px;height:120px;background:var(--band);overflow:hidden}
.footer-shade{position:absolute;left:0;top:0}
.contact{position:absolute;left:108px;top:42px;color:#fff;font-size:17px;font-weight:700;line-height:22px}
.contact div{display:flex;align-items:center;gap:10px}
.reach{position:absolute;right:61px;top:28px;text-align:right;color:#fff;font-weight:700}
.reach .phone{font-size:30px;line-height:36px}
.reach .web{font-size:19px}
</style>
</head>
<body>
<div class="hero" role="img" aria-label="Photo of a hand tapping a calculator over printed financial charts, with a pen and coffee cup in soft blue light"></div>

<div class="brand">
  <div class="brand-name"><span class="brand-dot"></span>larkfield</div>
  <div class="brand-sub">TAX AND ACCOUNTING INC.</div>
</div>
<div class="hero-tag">We know you can do the<br>Accounting, But do you want to?</div>

<div class="section-bar">Accounting Packages</div>
<div class="section-tag">We allow you to get back to what’s important.</div>

<section class="package develop">
  <h2>Develop
    <svg width="40" height="40" viewBox="0 0 40 40" fill="none" stroke="#b5b5b5" stroke-width="1.6"><circle cx="20" cy="20" r="7"/><path d="M20 3v6M20 31v6M3 20h6M31 20h6M8 8l4 4M28 28l4 4M8 32l4-4M28 12l4-4"/><circle cx="20" cy="20" r="13"/></svg>
  </h2>
  <ul class="list">
    <li>$300/mo when paid annually $325/mo billed monthly</li>
    <li>LedgerLine Online subscription</li>
    <li>Free accounting setup</li>
    <li>Weekly transaction processing</li>
    <li>Monthly account reconciliation <span class="note">(up to 2 accounts)</span></li>
    <li>Monthly financial statements by the 15<sup>th</sup> of the month</li>
  </ul>
</section>

<section class="package grow">
  <h2>Grow
    <svg width="44" height="38" viewBox="0 0 44 38" fill="none" stroke="#b5b5b5" stroke-width="2"><path d="M6 36V26M14 36V22M22 36V18M30 36V14M38 36V10"/><path d="M4 22L20 12l6 4L40 4"/></svg>
  </h2>
  <ul class="list">
    <li>$550/mo billed annually; $575/mo billed monthly</li>
    <li>LedgerLine Online subscription</li>
    <li>Free accounting setup</li>
    <li>Weekly transaction processing</li>
    <li>Monthly account reconciliation <span class="note">(up to 4 accounts)</span></li>
    <li>Monthly financial statements by the 10<sup>th</sup> of the month</li>
    <li>Client portal access for document sharing</li>
    <li>1 Custom Report</li>
    <li>Accounts Payable</li>
    <li>Monthly Scorecard</li>
    <li class="plain note">(customized metric tracking for your business)</li>
  </ul>
</section>

<section class="package relax">
  <h2>Relax <small>(We've Got This)</small>
    <svg width="46" height="30" viewBox="0 0 46 30" fill="none" stroke="#b5b5b5" stroke-width="2.4" stroke-linecap="round"><path d="M4 22h26l10-16"/><path d="M8 22l-3 7M30 22l3 7"/></svg>
  </h2>
  <ul class="list">
    <li>$850/mo billed annually; $875/mo billed monthly</li>
    <li>LedgerLine Online subscription</li>
    <li>Free accounting setup</li>
    <li>Weekly transaction processing</li>
    <li>Monthly account reconciliation <span class="note">(up to 5-10 accounts)</span></li>
    <li>Monthly financial statements by the 5<sup>th</sup> of the month</li>
    <li>Client portal access for document sharing</li>
    <li>2 Custom Reports</li>
    <li>Accounts Payable</li>
    <li>Invoicing and accounts receivable</li>
    <li>Weekly Scorecard</li>
    <li class="plain note">(customized metric tracking for your business)</li>
  </ul>
</section>

<section class="extras">
  <h2>Additional Options
    <svg width="38" height="38" viewBox="0 0 38 38" fill="none" stroke="#b5b5b5" stroke-width="1.8"><path d="M2 8h36M2 19h36M2 30h36"/><circle cx="24" cy="8" r="4" fill="#fff"/><circle cx="12" cy="19" r="4" fill="#fff"/><circle cx="28" cy="30" r="4" fill="#fff"/></svg>
  </h2>
  <div class="extras-grid">
    <div><h3>Payroll</h3><ul class="list"><li>1-10 employees $85/mo</li><li>11-30 employees $175/mo</li></ul></div>
    <div><h3>Corporate Taxes</h3><ul class="list"><li>$50/mo</li></ul></div>
    <div><h3>Sales Tax</h3><ul class="list"><li>$30/mo per state</li></ul></div>
    <div><h3>Owner Taxes</h3><ul class="list"><li>$25/mo</li></ul></div>
  </div>
</section>

<footer class="footer">
  <svg class="footer-shade" width="927" height="120" viewBox="0 0 927 120"><polygon points="0,0 590,0 660,120 0,120" fill="var(--band-light)"/></svg>
  <div class="contact">
    <div><svg width="14" height="18" viewBox="0 0 14 18"><path d="M7 0a7 7 0 0 0-7 7c0 5 7 11 7 11s7-6 7-11a7 7 0 0 0-7-7z" fill="#fff"/><circle cx="7" cy="7" r="2.6" fill="var(--band-light)"/></svg>4410 W. Maple Avenue, Fairview, KS 66000</div>
    <div><svg width="16" height="12" viewBox="0 0 16 12"><rect x="0.5" y="0.5" width="15" height="11" fill="none" stroke="#fff"/><path d="M0.5 0.5L8 7l7.5-6.5" fill="none" stroke="#fff"/></svg>hello@larkfield-tax.com</div>
  </div>
  <div class="reach">
    <div class="phone">(555) 014-2290</div>
    <div class="web">www.larkfieldtax.com</div>
  </div>
</footer>
</body>
</html>
```